Communication and Marketing agency needs a new presentation card

We are a group of communication and marketing agencies specialized in companies that are in the logistics and industrial sector. The head agency is TELVANO Grupo and the group consists of 4 agencies: TELVANO Media, TELVANO Digital, TELVANO Research and EnlazaPorImagen. We hace 4 offices in Spain (Madrid, Barcelona, Valencia and Murcia). We are looking for a clean and attractive design that transmits our experience, brand presence in the market and knowledge to those who receive the card.It has to maintain the colors of the logo that is attached.
Target Market(s)
logistics and industrial sector
Marketing department
Clean and attractive design

```html
<!DOCTYPE html>
<html lang="es">
<head>
<meta charset="utf-8">
<title>TELVANO – Tarjetas de presentación</title>
<link rel="stylesheet" href="https://fonts.googleapis.com/css2?family=Open+Sans:wght@400;600;700&display=swap">
<style>
  :root {
    --backdrop: #3a322e;
    --card: #1d1e20;
    --card-edge: #2a2b2e;
    --silver: #b9bbbe;
    --white: #f2f2f2;
    --red: #c8202b;
    --rule: #6e7074;
  }
  * { box-sizing: border-box; margin: 0; padding: 0; }
  html, body { width: 1200px; height: 864px; overflow: hidden; }
  body {
    background: var(--backdrop);
    font-family: "Open Sans", Arial, sans-serif;
    position: relative;
  }
  .card {
    position: absolute;
    width: 540px;
    height: 336px;
    background: var(--card);
    border: 1px solid var(--card-edge);
    box-shadow: 0 18px 40px rgba(0,0,0,.45);
    color: var(--white);
  }

  /* Back: group card */
  .card--group { left: 40px; top: 110px; }
  .group-brand {
    position: absolute; left: 0; right: 0; top: 82px;
    text-align: center;
    font-size: 46px; font-weight: 600; letter-spacing: 4px;
    color: var(--silver);
  }
  .group-rule {
    position: absolute; left: 0; right: 0; top: 190px;
    height: 1px; background: var(--rule);
  }
  .agency-list {
    position: absolute; left: 0; right: 0; top: 222px;
    display: flex; justify-content: space-around; align-items: center;
    list-style: none; padding: 0 18px;
  }
  .agency-list li {
    font-size: 14px; font-weight: 600; letter-spacing: .5px;
    color: var(--white); text-align: center; line-height: 1.2;
  }

  /* Front: personal card */
  .card--person { left: 620px; top: 418px; }
  .person-brand {
    position: absolute; left: 36px; top: 118px; width: 250px;
    text-align: center;
    font-size: 30px; font-weight: 600; letter-spacing: 2px;
    color: var(--red);
  }
  .person-divider {
    position: absolute; left: 300px; top: 70px;
    width: 1px; height: 170px; background: var(--rule);
  }
  .person-details { position: absolute; left: 322px; top: 78px; }
  .person-name { font-size: 20px; font-weight: 700; color: var(--red); }
  .person-role { font-size: 14px; margin-bottom: 10px; }
  .contact-list { list-style: none; }
  .contact-list li {
    display: flex; align-items: center; gap: 8px;
    font-size: 13.5px; line-height: 22px;
  }
  .contact-list svg { width: 12px; height: 12px; fill: var(--red); flex: none; }
  .office-list {
    position: absolute; left: 36px; bottom: 30px;
    display: flex; gap: 10px; align-items: center;
    list-style: none; font-size: 14px;
  }
  .office-list .dot { width: 5px; height: 5px; border-radius: 50%; background: var(--red); }
</style>
</head>
<body>

<section class="card card--group" aria-label="Reverso de la tarjeta">
  <div class="group-brand">TELVANO Grupo</div>
  <div class="group-rule"></div>
  <ul class="agency-list">
    <li>TELVANO<br>Digital</li>
    <li>TELVANO<br>Media</li>
    <li>TELVANO<br>Research</li>
    <li>EnlazaPor<br>Imagen</li>
  </ul>
</section>

<section class="card card--person" aria-label="Anverso de la tarjeta">
  <div class="person-brand">TELVANO Media</div>
  <div class="person-divider"></div>
  <div class="person-details">
    <p class="person-name">Ramiro Ostalé</p>
    <p class="person-role">Director</p>
    <ul class="contact-list">
      <li><svg viewBox="0 0 12 12"><path d="M1 3c0-1 1-2 2-2h6c1 0 2 1 2 2v1H8V3H4v1H1zM2 5h8l1 6H1z"/></svg>910 555 214</li>
      <li><svg viewBox="0 0 12 12"><path d="M3 0h6v12H3zM4 1v8h4V1z"/></svg>600 555 718</li>
      <li><svg viewBox="0 0 12 12"><path d="M0 2h12v8H0zM1 3l5 4 5-4z"/></svg>rostale@telvano.es</li>
      <li><svg viewBox="0 0 12 12"><path d="M1 1h10v7H5l-3 3V8H1z"/></svg>ramiroostale</li>
      <li><svg viewBox="0 0 12 12"><circle cx="6" cy="6" r="5.5"/></svg>telvano.es</li>
    </ul>
  </div>
  <ul class="office-list">
    <li>Madrid</li><li class="dot"></li>
    <li>Barcelona</li><li class="dot"></li>
    <li>Valencia</li><li class="dot"></li>
    <li>Murcia</li>
  </ul>
</section>

</body>
</html>
```